Small Business Broker Business Card Design

A business card design for a small business brokerage, which is a financial service, not unlike real estate brokerage, but for small businesses such as laundromats, pizza shops, restaurants, cleaners etc. The designs should all be simple, more conservative in nature, using the colors and font of the logo. Again, think real estate Brokerage as a business context
Contact Information for Business Card
Name: Milo R. Dunbar. Title: Small Business Advisor. Email: m.dunbar@harborstoneadvisory.com. Mobile: (917) 555-0148. Office: (718) 555-0193. www.harborstoneadvisory.com

```html
<!DOCTYPE html>
<html lang="en">
<head>
<meta charset="utf-8">
<title>Harborstone Advisory — Business Card</title>
<link rel="stylesheet" href="https://fonts.googleapis.com/css2?family=Michroma&family=Poppins:wght@400;500&display=swap">
<style>
  :root {
    --navy: #173a6b;
    --navy-light: #2f5285;
    --green: #8cc63f;
    --white: #ffffff;
    --stage: #e9eaec;
    --brand-font: "Michroma", sans-serif;
    --body-font: "Poppins", sans-serif;
  }
  * { margin: 0; padding: 0; box-sizing: border-box; }
  html, body { width: 1200px; height: 716px; overflow: hidden; }
  body {
    background: var(--stage);
    display: flex;
    align-items: center;
    justify-content: center;
    gap: 40px;
  }
  .card {
    position: relative;
    width: 540px;
    height: 309px;
    overflow: hidden;
    box-shadow: 0 6px 18px rgba(0,0,0,0.18);
  }
  .card--front { background: var(--navy); }
  .card--back { background: var(--white); }

  .brand {
    position: absolute;
    display: flex;
    flex-direction: column;
    align-items: center;
    text-align: center;
  }
  .brand__mark {
    width: 14px; height: 14px;
    margin-bottom: 12px;
    background: var(--green);
  }
  .brand__name {
    font-family: var(--brand-font);
    font-size: 17px;
    letter-spacing: 0.5px;
    text-transform: uppercase;
  }
  .brand__tagline {
    font-family: var(--brand-font);
    font-size: 8.5px;
    letter-spacing: 1px;
    text-transform: uppercase;
    color: var(--green);
    margin-top: 5px;
  }
  .card--front .brand { left: 0; right: 0; top: 112px; }
  .card--front .brand__name { color: var(--white); }

  .card--back .brand { left: 80px; top: 34px; width: 320px; }
  .card--back .brand__name { color: var(--navy); font-size: 13px; }
  .card--back .brand__tagline { font-size: 6.5px; }
  .card--back .brand__mark { width: 11px; height: 11px; margin-bottom: 9px; }

  .back-band { position: absolute; inset: 0; }

  .contact {
    position: absolute;
    right: 82px;
    top: 194px;
    text-align: right;
    color: var(--white);
    font-family: var(--body-font);
  }
  .contact__name {
    font-family: var(--brand-font);
    color: var(--green);
    font-size: 14px;
    line-height: 18px;
    text-transform: uppercase;
    letter-spacing: 0.5px;
  }
  .contact__title { font-size: 10.5px; margin-bottom: 6px; }
  .contact__list { list-style: none; font-size: 10.5px; line-height: 16px; }
  .contact__list li { display: flex; justify-content: flex-end; align-items: center; gap: 6px; }
  .contact__icon { width: 10px; height: 10px; fill: var(--green); }
</style>
</head>
<body>
  <section class="card card--front" aria-label="Card front">
    <div class="brand">
      <span class="brand__mark"></span>
      <span class="brand__name">Harborstone Advisory, Inc</span>
      <span class="brand__tagline">Trusted guidance for every local business sale</span>
    </div>
  </section>

  <section class="card card--back" aria-label="Card back">
    <svg class="back-band" viewBox="0 0 540 309" width="540" height="309" aria-hidden="true">
      <defs>
        <linearGradient id="bandShade" x1="0" y1="0" x2="1" y2="1">
          <stop offset="0" stop-color="#2f5285"/>
          <stop offset="0.6" stop-color="#173a6b"/>
        </linearGradient>
      </defs>
      <polygon points="0,122 425,162 540,222 540,309 0,309" fill="url(#bandShade)"/>
    </svg>

    <div class="brand">
      <span class="brand__mark"></span>
      <span class="brand__name">Harborstone Advisory, Inc</span>
      <span class="brand__tagline">Trusted guidance for every local business sale</span>
    </div>

    <div class="contact">
      <div class="contact__name">Milo R. Dunbar</div>
      <div class="contact__title">Small Business Advisor</div>
      <ul class="contact__list">
        <li>(718) 555-0193
          <svg class="contact__icon" viewBox="0 0 10 10"><path d="M1 3c0-1 1-2 4-2s4 1 4 2v1H7V3H3v1H1zM2 5h6l1 4H1z"/></svg></li>
        <li>(917) 555-0148
          <svg class="contact__icon" viewBox="0 0 10 10"><path d="M3 0h4a1 1 0 0 1 1 1v8a1 1 0 0 1-1 1H3a1 1 0 0 1-1-1V1a1 1 0 0 1 1-1zm0 1.5v6h4v-6z"/></svg></li>
        <li>m.dunbar@harborstoneadvisory.com
          <svg class="contact__icon" viewBox="0 0 10 10"><path d="M0 2h10v6H0zM1 3l4 3 4-3z" fill-rule="evenodd"/></svg></li>
        <li>www.harborstoneadvisory.com
          <svg class="contact__icon" viewBox="0 0 10 10"><circle cx="5" cy="5" r="4.5"/></svg></li>
      </ul>
    </div>
  </section>
</body>
</html>
```